Flyer for annual KESTREL SUMMIT 2020

I would like a church event flyer designed. The event is called "KESTREL SUMMIT 2020". I am looking for a professional, yet catchy design that uses our brand colors and logo creatively while communicating key information of the event effectively.

1. The logo is attached in two color formats. The designer has the choice to use them as he/she want.

2. The location of the event is: Harlow Community Center, 239 Fennimore Street, Portland, ME 04117

3. Time and date of event. The designer can organize and format the date and time as he/she pleases.
Thursday December 31st @ 6:30PM
Friday January 1st @ 6:30PM
Saturday 2nd @ 6:30PM
Sunday 3rd @ 4:30PM

4. The topic of the event is "In Fire and On Fire". The designer is free to use this phrase as he/she pleases to create a good composition.

5. Speaker: Prophet Marcus Olunde (2 pictures of the speaker to choose from are attached)

6. Contact information: contact@brightmeadowfold.org - Telephone number: 207 583 2914

7. I would also like the following three words on the flyer. These words describe the focus of the event: FIRE, REVIVAL, PROPHETIC

Target Market(s)

Young adults

Font styles to use
Sans Serif

Requirements
Must have
• Logo, speaker's picture
Should not have
• cross image, church image

```html
<!DOCTYPE html>
<html lang="en">
<head>
<meta charset="utf-8">
<title>Kestrel Summit 2020 Flyer</title>
<link href="https://fonts.googleapis.com/css2?family=Montserrat:ital,wght@0,600;0,700;0,800;1,800&family=Open+Sans:wght@400;600&display=swap" rel="stylesheet">
<style>
  :root {
    --amber: #f2a22c;
    --flame-red: #d63b19;
    --bar-red: #d84a1f;
    --navy: #1d3a6e;
    --ink: #2d2d2d;
    --white: #ffffff;
    --photo-light: #e9edf0;
    --photo-mid: #c9c4bf;
    --photo-warm: #a0705a;
  }
  * { margin: 0; padding: 0; box-sizing: border-box; }
  html, body { width: 846px; height: 1200px; overflow: hidden; background: var(--white); }
  .flyer {
    position: relative;
    width: 846px;
    height: 1200px;
    overflow: hidden;
    background: var(--white);
    font-family: "Open Sans", Arial, sans-serif;
  }
  .speaker-photo {
    position: absolute;
    left: 0; top: 0;
    width: 846px; height: 820px;
    background: linear-gradient(100deg, var(--photo-light) 0%, var(--photo-light) 40%, var(--photo-mid) 62%, var(--photo-warm) 82%, #6b5448 100%);
  }
  .shapes { position: absolute; left: 0; top: 0; }
  .brand {
    position: absolute;
    left: 63px; top: 140px;
    display: flex; align-items: center; gap: 14px;
  }
  .brand-dot { width: 26px; height: 26px; border-radius: 50%; background: var(--amber); }
  .brand-name {
    font-family: "Montserrat", Arial, sans-serif;
    font-weight: 700;
    font-size: 60px;
    letter-spacing: 2px;
    color: var(--navy);
  }
  .event-title {
    position: absolute;
    left: 48px; top: 520px;
    font-family: "Montserrat", Arial, sans-serif;
    font-weight: 700;
    color: var(--white);
    line-height: 1;
  }
  .event-title .line-1 { display: block; font-size: 66px; letter-spacing: 1px; }
  .event-title .line-2 { display: block; font-size: 50px; margin-top: 8px; letter-spacing: 1px; }
  .event-title .line-3 { display: block; font-size: 92px; margin-top: 2px; letter-spacing: 2px; }
  .speaker {
    position: absolute;
    left: 48px; top: 778px;
    width: 374px;
    padding-bottom: 8px;
    border-bottom: 1.5px solid var(--white);
    font-size: 18px;
    color: var(--white);
    letter-spacing: 0.3px;
  }
  .topic {
    position: absolute;
    left: 48px; top: 826px;
    font-size: 20px;
    line-height: 27px;
    color: var(--flame-red);
    letter-spacing: 0.3px;
  }
  .schedule {
    position: absolute;
    left: 48px; top: 903px;
    list-style: none;
    font-size: 17px;
    line-height: 24px;
    color: var(--ink);
  }
  .location-label {
    position: absolute;
    left: 48px; top: 1034px;
    font-size: 17px;
    font-weight: 600;
    color: var(--white);
  }
  .focus-words {
    position: absolute;
    left: 462px; top: 812px;
    font-family: "Montserrat", Arial, sans-serif;
    font-style: italic;
    font-weight: 800;
    font-size: 58px;
    line-height: 74px;
    color: var(--flame-red);
    letter-spacing: -1px;
  }
  .contact-bar {
    position: absolute;
    left: 0; top: 1060px;
    width: 846px; height: 94px;
    background: var(--bar-red);
  }
  .address {
    position: absolute;
    left: 48px; top: 16px;
    font-size: 17px;
    line-height: 26px;
    letter-spacing: 1.2px;
    color: var(--white);
    font-style: normal;
  }
  .contact-item {
    position: absolute;
    left: 486px;
    display: flex; align-items: center; gap: 12px;
    color: var(--white);
  }
  .contact-email { top: 18px; font-size: 17px; }
  .contact-phone { top: 58px; font-size: 22px; letter-spacing: 1.5px; }
</style>
</head>
<body>
<div class="flyer">
  <div class="speaker-photo" role="img" aria-label="Photo of the speaker in an orange blazer seated by a window"></div>

  <svg class="shapes" width="846" height="1200" viewBox="0 0 846 1200" aria-hidden="true">
    <polygon points="0,478 545,432 482,1060 0,1060" fill="#f2a22c" fill-opacity="0.92"/>
    <polygon points="478,762 846,652 846,1060 478,1060" fill="#ffffff"/>
  </svg>

  <div class="brand">
    <span class="brand-dot"></span>
    <span class="brand-name">VELORA</span>
  </div>

  <h1 class="event-title">
    <span class="line-1">KESTREL</span>
    <span class="line-2">SUMMIT</span>
    <span class="line-3">2020</span>
  </h1>

  <p class="speaker">SPEAKER: PROPHET MARCUS OLUNDE</p>

  <p class="topic">THE TOPIC OF THE EVENT IS<br>"IN&nbsp; FIRE&nbsp; AND&nbsp; ON&nbsp; FIRE".</p>

  <ul class="schedule">
    <li>Thursday December 31st @ 6:30PM</li>
    <li>Friday January 1st @ 6:30PM</li>
    <li>Saturday 2nd&nbsp; @&nbsp; 6:30PM</li>
    <li>Sunday 3rd&nbsp; @&nbsp; 4:30PM</li>
  </ul>

  <p class="location-label">THE LOCATION OF THE EVENT IS:</p>

  <p class="focus-words">FIRE,<br>REVIVAL,<br>PROPHETIC</p>

  <div class="contact-bar">
    <address class="address">Harlow Community Center,<br>239 Fennimore Street,<br>Portland, ME 04117</address>
    <div class="contact-item contact-email">
      <svg width="34" height="22" viewBox="0 0 34 22" aria-hidden="true">
        <rect x="1" y="1" width="32" height="20" fill="none" stroke="#fff" stroke-width="1.8"/>
        <polyline points="1,1 17,13 33,1" fill="none" stroke="#fff" stroke-width="1.8"/>
      </svg>
      <span>contact@brightmeadowfold.org</span>
    </div>
    <div class="contact-item contact-phone">
      <svg width="22" height="22" viewBox="0 0 24 24" aria-hidden="true">
        <path fill="#fff" d="M6.6 10.8c1.4 2.8 3.8 5.1 6.6 6.6l2.2-2.2c.3-.3.7-.4 1-.2 1.1.4 2.3.6 3.6.6.6 0 1 .4 1 1V20c0 .6-.4 1-1 1C10.6 21 3 13.4 3 4c0-.6.4-1 1-1h3.5c.6 0 1 .4 1 1 0 1.3.2 2.5.6 3.6.1.3 0 .7-.2 1z"/>
      </svg>
      <span>207 583 2914</span>
    </div>
  </div>
</div>
</body>
</html>
```